V9 Web Design Project

New company website for Intel cyber security company.

Style should be cool, but remain appropriate for very serious subject matter and audience.

Target Market(s)

Target audience is government and the military

Navigation needs to include:
- About Us
- Services
- Careers
- Contact Us
- Contracts

As well as 2 feature areas - use "Technology Integration" and "Case Study" as the supporting headlines.

Industry/Entity Type

Security

Font styles to use
Sans Serif

Colors

Designer to choose colors to be used in the design.

Requirements
Must have
• Mountain imagery and theme.

Use logo attached.

New Tagline - "Securing the Continuum"
Nice to have
• Supporting imagery could include photos representative of security - avoid cliches.
Should not have
• Needs to be serious not frivolous

```html
<!DOCTYPE html>
<html lang="en">
<head>
<meta charset="utf-8">
<title>V9 Group – Securing the Continuum</title>
<link rel="stylesheet" href="https://fonts.googleapis.com/css2?family=Lora:wght@400;700&family=Oswald:wght@400;500&family=Open+Sans:wght@400;600;700&display=swap">
<style>
:root{
  --navy:#1f2d66;
  --blue:#2f63ad;
  --sky:#4a7cc0;
  --ink:#2b2b2b;
  --muted:#555;
  --light:#f2f2f2;
  --line:#d8d8d8;
  --dark:#1b1b1b;
  --darker:#111;
  --white:#fff;
}
*{box-sizing:border-box;margin:0;padding:0}
html,body{width:1200px;height:2956px;overflow:hidden}
body{font-family:"Open Sans",Arial,sans-serif;color:var(--ink);background:var(--white);position:relative}
section,header,footer{position:relative;width:1200px;overflow:hidden}
.abs{position:absolute}

/* hero */
.hero{height:733px;background:linear-gradient(180deg,#4f76a8 0%,#7397c4 30%,#a9c0dc 55%,#5b83b8 80%,#3f6aa5 100%)}
.hero-photo{position:absolute;inset:0;background:radial-gradient(ellipse at 50% 40%,rgba(255,255,255,.35),rgba(255,255,255,0) 60%)}
.logo{left:36px;top:22px;display:flex;align-items:center;gap:16px;color:var(--white)}
.logo-mark{width:76px;height:76px;background:#2a3e6a;border:2px solid rgba(255,255,255,.7)}
.logo-name{font-family:"Lora",serif;font-size:46px;letter-spacing:1px}
.nav{right:36px;top:38px;display:flex;gap:36px;font-size:17px;color:var(--white);text-transform:uppercase}
.nav a{color:inherit;text-decoration:none;padding-bottom:8px}
.nav .active{border-bottom:2px solid var(--white)}
.hero-copy{left:0;width:1200px;top:250px;text-align:center;color:var(--white)}
.hero-lead{font-family:"Lora",serif;font-size:34px;line-height:32px}
.tagline{font-family:"Oswald",sans-serif;font-size:64px;letter-spacing:1px;margin:44px auto 0;display:inline-block;padding:6px 0;border-top:2px solid rgba(255,255,255,.8);border-bottom:2px solid rgba(255,255,255,.8);line-height:76px}
.hero-sub{font-family:"Lora",serif;font-size:38px;line-height:50px;margin-top:28px}

/* welcome */
.welcome{height:367px;text-align:center}
.welcome h1{font-weight:400;font-size:40px;margin-top:56px;color:var(--ink);letter-spacing:1px}
.welcome h1 span{font-family:"Lora",serif;color:var(--navy)}
.welcome h1::after{content:"";display:block;width:380px;height:2px;background:var(--line);margin:10px auto 0}
.intro{color:var(--blue);font-size:18px;margin-top:22px}
.body{font-size:15px;line-height:29px;color:var(--ink);width:1130px;margin:14px auto 0}
.btn{display:inline-block;background:var(--navy);color:var(--white);font-size:15px;font-weight:600;padding:10px 28px;margin-top:36px;border-radius:3px}

/* features */
.features{height:343px;background:linear-gradient(180deg,#e9e9e9,#f6f6f6 40%,#e4e4e4);border-top:1px solid var(--line)}
.sec-title{width:1200px;text-align:center;font-size:38px;font-weight:400;letter-spacing:1px;color:var(--ink)}
.sec-title span{color:var(--navy)}
.features .sec-title{position:absolute;top:34px}
.feature{top:106px;width:528px;height:177px;background:var(--white);border-radius:6px;box-shadow:0 2px 6px rgba(0,0,0,.12);display:flex;gap:22px;padding:18px 24px}
.feature-icon{flex:none;width:138px;height:138px;border-radius:50%;background:var(--sky);border:8px solid #dbe4f1;display:flex;align-items:center;justify-content:center}
.feature h2{font-weight:400;font-size:29px;color:var(--navy);margin-top:6px}
.feature p{font-size:15px;line-height:24px;margin-top:10px}

/* services */
.services{height:591px;background:linear-gradient(160deg,#0f1b2c,#16253a 50%,#0c1522)}
.services .sec-title{position:absolute;top:48px;color:var(--white)}
.service{top:118px;width:346px;height:434px;background:var(--white);border-radius:6px;overflow:hidden}
.service-img{height:227px}
.service h3{height:50px;background:var(--navy);color:var(--white);font-weight:400;font-size:23px;text-align:center;line-height:50px}
.service p{font-size:15px;line-height:24px;padding:16px 14px 0}
.more{display:block;text-align:center;color:var(--blue);font-size:14px;margin-top:20px}

/* testimonial */
.clients{height:301px}
.clients .sec-title{position:absolute;top:42px}
.quote{left:36px;top:103px;width:1128px;height:124px;background:#eef1f8;border:1px solid #d6dbe8;border-radius:4px;padding:14px 26px 0 44px;font-size:15px;line-height:29px}
.quote::before{content:"“";position:absolute;left:14px;top:-6px;font-family:"Lora",serif;font-size:56px;color:var(--navy)}
.quote::after{content:"";position:absolute;right:28px;bottom:-16px;border:8px solid transparent;border-top-color:#d6dbe8}
.author{right:42px;top:239px;font-size:14px;color:var(--navy)}

/* partners */
.partners{height:172px;background:var(--light);border-top:1px solid var(--line)}
.partner{top:47px;width:174px;height:95px;background:var(--white);border:1px solid var(--line);display:flex;align-items:center;justify-content:center;font-size:22px;font-weight:700;color:#8a8a8a}

/* footer */
.site-footer{height:390px;background:#1d1d1d;color:#cfcfcf}
.site-footer h4{font-weight:400;font-size:31px;color:var(--white)}
.contact{left:36px;top:44px;width:534px}
.contact h4{border-bottom:1px solid #444;padding-bottom:12px}
.contact-list{margin-top:30px;font-size:14px;line-height:22px;list-style:none;width:220px}
.contact-list li{display:flex;gap:10px;margin-bottom:26px}
.map{left:291px;top:118px;width:249px;height:219px;background:linear-gradient(135deg,#e8e6df,#d5d9d0);border:3px solid var(--white)}
.inquiry{left:630px;top:44px;width:534px}
.field{position:absolute;background:#3d3d3d;border:1px solid #555;font-size:13px;color:#aaa;padding:6px 10px;height:36px}
.send{position:absolute;left:6px;top:382px;width:114px;height:30px;background:var(--white);color:var(--ink);font-size:15px;text-align:center;line-height:30px;border-radius:3px}
.bottom-bar{height:59px;background:var(--darker);color:#999;font-size:14px}
.bottom-nav{left:36px;top:19px;display:flex;gap:0}
.bottom-nav a{color:#999;text-decoration:none;padding:0 20px;border-right:1px solid #444}
.bottom-nav a:first-child{padding-left:0;color:var(--white)}
.bottom-nav a:last-child{border:none}
.social{left:672px;top:16px;display:flex;gap:8px}
.social span{width:24px;height:24px;border-radius:50%;background:#4a6ea8}
.copy{right:36px;top:19px}
</style>
</head>
<body>

<header class="hero">
  <div class="hero-photo" role="img" aria-label="Snow-capped mountain range under a blue sky, tinted blue"></div>
  <div class="abs logo"><div class="logo-mark"></div><span class="logo-name">V9 GROUP</span></div>
  <nav class="abs nav">
    <a class="active" href="#">Home</a><a href="#">About Us</a><a href="#">Services</a><a href="#">Careers</a><a href="#">Contact Us</a><a href="#">Contracts</a>
  </nav>
  <div class="abs hero-copy">
    <p class="hero-lead">We Provide Cyber Security Services<br>Government And Military</p>
    <h2 class="tagline">SECURING THE CONTINUUM</h2>
    <p class="hero-sub">Vel Um Dolore Eu Feugiat Nulla<br>Facilisis At Vero Eros</p>
  </div>
</header>

<section class="welcome">
  <h1>WELCOME TO <span>V9 GROUP</span></h1>
  <p class="intro">With the proliferation of Internet-enabled devices, cyber culture is growing more rapidly than cyber security.</p>
  <p class="body">Lorem ipsum dolor sit amet, consectetuer adipiscing elit, sed diam nonummy nibh euismod tincidunt ut laoreet dolore magna aliquam erat volutpat. Ut wisi enim ad minim veniam, quis nostrud exerci tation ullamcorper suscipit lobortis nisl aliquip ex ea commodo consequat. Duis ro eros et accumsan et iusto odio dignissim qui blandit praesent luptatum zzril delenit augue duis dolore .</p>
  <span class="btn">Read More</span>
</section>

<section class="features">
  <h2 class="sec-title">FEATURE <span>AREAS</span></h2>
  <div class="abs feature" style="left:36px">
    <div class="feature-icon"><svg width="64" height="64" viewBox="0 0 64 64" fill="none" stroke="#fff" stroke-width="4"><circle cx="32" cy="14" r="8"/><circle cx="14" cy="46" r="8"/><circle cx="50" cy="46" r="8"/><path d="M28 21 18 39M36 21l10 18M22 46h20"/></svg></div>
    <div><h2>Technology Integration</h2><p>Lorem ipsum dolor sit amet, consectetuer iw adipiscing elit, sed diam nonummy nibh euismod tincidunt ut laoreet dolore.</p></div>
  </div>
  <div class="abs feature" style="left:636px">
    <div class="feature-icon"><svg width="64" height="64" viewBox="0 0 64 64" fill="none" stroke="#fff" stroke-width="4"><rect x="8" y="8" width="30" height="22"/><path d="M32 36v8M14 44h36M14 44v8M32 44v8M50 44v8"/><circle cx="14" cy="56" r="3"/><circle cx="32" cy="56" r="3"/><circle cx="50" cy="56" r="3"/></svg></div>
    <div><h2>Case Study</h2><p>Lorem ipsum dolor sit amet, consectetuer iw adipiscing elit, sed diam nonummy nibh euismod tincidunt ut laoreet dolore.</p></div>
  </div>
</section>

<section class="services" role="region" aria-label="Our services">
  <h2 class="sec-title">OUR SERVICES</h2>
  <div class="abs service" style="left:36px">
    <div class="service-img" role="img" aria-label="Blue digital network scene with a padlock" style="background:linear-gradient(160deg,#1d6fd0,#0d2f6e)"></div>
    <h3>Web Application Security</h3>
    <p>Ut wisi enim ad minim veniam, quis nostrp exerci tation ullamcorper suscipit lobortio nisl aliquip exea commodo consequat.</p>
    <span class="more">Read More »</span>
  </div>
  <div class="abs service" style="left:426px">
    <div class="service-img" role="img" aria-label="Circuit board with a glowing padlock" style="background:linear-gradient(160deg,#3a5fae,#111c3a)"></div>
    <h3>Vulnerability Assessment</h3>
    <p>Ut wisi enim ad minim veniam, quis nostrp exerci tation ullamcorper suscipit lobortio nisl aliquip exea commodo consequat.</p>
    <span class="more">Read More »</span>
  </div>
  <div class="abs service" style="left:816px">
    <div class="service-img" role="img" aria-label="Smartphone showing a padlock over security text" style="background:linear-gradient(160deg,#b9b4ad,#6d6a66)"></div>
    <h3>Mobile Application Security</h3>
    <p>Ut wisi enim ad minim veniam, quis nostrp exerci tation ullamcorper suscipit lobortio nisl aliquip exea commodo consequat.</p>
    <span class="more">Read More »</span>
  </div>
</section>

<section class="clients">
  <h2 class="sec-title">WHAT OUR <span>CLIENTS SAYING</span></h2>
  <div class="abs quote">Lorem ipsum dolor sit amet, consectetuer adipiscing elit, sed diam nonummy nibh euismod tincidunt ut laoreet dolore magna aliquam erat into involutpat. Ut wisi enim ad minim veniam, quis nostrud exerci tation ullamcorper suscipit lobortis nisl aliquip ex ea commodo consequat. Duis ro eros et accumsan et iusto odio dignissim qui blandit praesent luptatum zzril delenit augue duis dolore .</div>
  <p class="abs author">Mr. Daniel Ardent Center Manager</p>
</section>

<section class="partners">
  <div class="abs partner" style="left:42px">Harbor Works</div>
  <div class="abs partner" style="left:276px">Northfield</div>
  <div class="abs partner" style="left:510px">Crestline</div>
  <div class="abs partner" style="left:750px">Northfield</div>
  <div class="abs partner" style="left:984px">Bluepeak</div>
</section>

<footer class="site-footer">
  <div class="abs contact">
    <h4>Location Information</h4>
    <ul class="contact-list">
      <li><svg width="14" height="18" viewBox="0 0 14 18"><path d="M7 0a7 7 0 0 0-7 7c0 5 7 11 7 11s7-6 7-11a7 7 0 0 0-7-7z" fill="#aaa"/><circle cx="7" cy="7" r="2.5" fill="#1d1d1d"/></svg><span>V9 GROUP<br>Opp Old Post Office, Rd. No. 12, Ridge Estate, Westvale – 400210</span></li>
      <li><svg width="16" height="16" viewBox="0 0 16 16"><path d="M3 1l3 3-2 2c1 2 3 4 5 5l2-2 3 3-2 3C6 14 2 10 1 3z" fill="#aaa"/></svg><span>Phone: 555-014-2290</span></li>
      <li><svg width="16" height="12" viewBox="0 0 16 12"><rect width="16" height="12" fill="#aaa"/><path d="M0 0l8 6 8-6" stroke="#1d1d1d" fill="none"/></svg><span>Email: info@v9group.com</span></li>
    </ul>
  </div>
  <div class="abs map" role="img" aria-label="Street map showing the office location"></div>
  <div class="abs inquiry">
    <h4>QUICK INQUIRY</h4>
    <div class="field" style="left:6px;top:77px;width:528px">Name</div>
    <div class="field" style="left:6px;top:134px;width:254px">Email</div>
    <div class="field" style="left:280px;top:134px;width:254px">Phone</div>
    <div class="field" style="left:6px;top:176px;width:528px;height:64px">Message</div>
    <div class="send">SEND</div>
  </div>
</footer>

<div class="bottom-bar" style="position:relative">
  <nav class="abs bottom-nav"><a href="#">Home</a><a href="#">About Us</a><a href="#">Services</a><a href="#">Contact Us</a><a href="#">Contracts</a></nav>
  <div class="abs social"><span></span><span></span><span></span><span></span><span></span></div>
  <p class="abs copy">©2015 v9group. All Rights Reserved</p>
</div>

</body>
</html>
```